Bright Path Attorneys Billboard Design for Personal Injury Law Firm

Need a billboard design that we can use for different versions. 1400px X 400px jpeg or png
I have attached the logo and the attorney for the billboard. Attorney Marla Benning
Here is a link to our current website brightpathlegalgroup.example

HEADLINE: HIT BY A TRUCK?
SUBHEAD: NO FEE. BIG FIGHT.
877-GRANTLY

HEADLINE: ACCIDENT?
SUBHEAD: NO FEE, UNLESS WE WIN!
877-GRANTLY

HEADLINE: BIG TRUCK. BIG CASE.
SUBHEAD: YOU PAY $0 UPFRONT
877-GRANTLY

Target Market(s)

People in Car Accident

Industry/Entity Type

Personal Injury Attorneys

```html
<!DOCTYPE html>
<html lang="en">
<head>
<meta charset="utf-8">
<title>Bright Path Attorneys – Hit By A Truck Billboard</title>
<link rel="stylesheet" href="https://fonts.googleapis.com/css2?family=Archivo:ital,wdth,wght@0,62..125,100..900;1,62..125,100..900&display=swap">
<style>
  :root {
    --board-black: #000000;
    --signal-yellow: #eeff00;
    --text-white: #ffffff;
    --photo-dark: #121317;
    --photo-mid: #262830;
    --photo-warm: #3a2a22;
  }
  * { margin: 0; padding: 0; box-sizing: border-box; }
  html, body {
    width: 1200px;
    height: 343px;
    overflow: hidden;
    background: var(--board-black);
  }
  .billboard {
    position: relative;
    width: 1200px;
    height: 343px;
    overflow: hidden;
    background: var(--board-black);
    font-family: "Archivo", "Helvetica Neue", Arial, sans-serif;
  }
  .truck-photo {
    position: absolute;
    top: 0;
    right: 0;
    width: 500px;
    height: 343px;
    background: linear-gradient(160deg, var(--photo-mid) 0%, var(--photo-warm) 50%, var(--photo-dark) 100%);
    -webkit-mask-image: linear-gradient(90deg, transparent 0%, #000 35%);
            mask-image: linear-gradient(90deg, transparent 0%, #000 35%);
  }
  .brand {
    position: absolute;
    top: 36px;
    left: 47px;
    display: flex;
    align-items: center;
    gap: 10px;
    color: var(--text-white);
    font-weight: 600;
    font-size: 22px;
    line-height: 28px;
    letter-spacing: 0.3px;
  }
  .brand-dot {
    width: 16px;
    height: 16px;
    border-radius: 50%;
    background: var(--text-white);
  }
  .headline { font-size: inherit; }
  .headline-line,
  .subhead {
    position: absolute;
    white-space: nowrap;
  }
  .headline-line {
    color: var(--signal-yellow);
    font-weight: 900;
    font-style: italic;
    font-stretch: 100%;
    font-size: 112px;
    line-height: 1;
    letter-spacing: -1px;
    transform: translate(-50%, -50%) rotate(-13deg) skewX(-12deg) scaleX(0.86);
  }
  .headline-line--top { left: 499px; top: 98px; }
  .headline-line--bottom { left: 640px; top: 172px; }
  .subhead {
    left: 662px;
    top: 265px;
    color: var(--text-white);
    font-weight: 600;
    font-size: 37px;
    line-height: 1;
    transform: translate(-50%, -50%) rotate(-8deg);
  }
  .phone {
    position: absolute;
    right: 26px;
    top: 275px;
    color: var(--signal-yellow);
    font-weight: 800;
    font-stretch: 88%;
    font-size: 66px;
    line-height: 1;
  }
</style>
</head>
<body>
  <div class="billboard">
    <div class="truck-photo" role="img" aria-label="Photo of a semi truck cab at sunset"></div>

    <div class="brand">
      <span class="brand-dot"></span>
      <span class="brand-name">Bright Path Attorneys</span>
    </div>

    <h1 class="headline">
      <span class="headline-line headline-line--top">HIT BY A</span>
      <span class="headline-line headline-line--bottom">TRUCK</span>
    </h1>

    <p class="subhead">NO FEE. BIG FIGHT.</p>

    <p class="phone">877-GRANTLY</p>
  </div>
</body>
</html>
```